Buch-/E-Book-Cover Ratgeber Selbstliebe
Zielgruppe
Ich suche ein ansprechendes Cover-Design für mein E-Book. Es handelt sich um einen Ratgeber über Selbstliebe und meine Zielgruppe sind Frauen im Alter zwischen 18 und 40 Jahren.
Aufgabenstellung
Klare Designs, die das Thema des Ratgebers unterstreichen und nicht durch unnötige Details und unlesbare Verschnörkelungen ablenken. Die weibliche Zielgruppe sollte vor allem angesprochen werden, dies sollte auch in der Farbauswahl berücksichtigt werden. Das bedeutet helle Farbtöne wie rosa, rot, hellblau oder pastellgelb.
Die Umsetzung des Motivs überlasse ich der Kreativität des Designers. Es können sowohl Stockfotos von einer jungen Frau gewählt werden, die Freude ausstrahlt und sich wohl in ihrer Haut fühlt (wo vielleicht auch warmes Licht oder Sonnenschein auf dem Cover zu sehen sind) oder ein rein graphisches Bild aus zusammengesetzten Elementen, die eine junge Frau zeigen und ihre Beziehung zur Selbstliebe deutlich wird. Es muss nicht zwangsläufig ein Herz abgebildet werden, nur weil es das erste ist, was man vielleicht mit Liebe assoziiert, auch wenn ein kreativer Umgang mit dem Herz als Symbol eine durchaus ansprechende Wirkung haben kann. Wichtig wäre mir eine kreative Umsetzung im Bild, wodurch das Thema der 'Selbstliebe' sofort deutlich wird und den Käufer anspricht. Der Titel sollte genauso deutlich hervorstechen wie das zentrale Motiv. Außerdem sollte gleich erkennbar sein, dass es sich nicht um einen Roman, sondern um einen Ratgeber handelt. Daher bin ich an einer graphischen Aufbereitung genauso wie an einem Fotomotiv interessiert. Bereits existierende Cover zu einem ähnlichen Ratgeber- Thema, die ich ansprechend finde, füge ich im Anhang hinzu.
Bitte nicht die im Anhang eingefügten Dateien verwenden, da sie urheberrechtlich geschützt sind! Sie dienen nur als Interpretationsvorschlag.
Titel: Innere Ruhe finden
Untertitel: Wie aus kleinen Gewohnheiten jeden Tag neue Gelassenheit im Alltag wächst
Autorenname: Jana Roth
Der Buchrücken soll farblich an das Cover angepasst werden. Der Buchrückentext folgt noch im Anhang.
Das E-Book wird es auch als Paperback Buch geben. Der Umfang des Ra..

```html
<!DOCTYPE html>
<html lang="de">
<head>
<meta charset="utf-8">
<title>Innere Ruhe finden – Jana Roth</title>
<link rel="stylesheet" href="https://fonts.googleapis.com/css2?family=Josefin+Sans:wght@100;200;300&family=Dancing+Script:wght@700&display=swap">
<style>
  :root {
    --backdrop: #ececec;
    --cover: #5f7573;
    --cover-light: #677d7b;
    --cover-dark: #566b69;
    --ink-light: #f2efee;
    --rose: #b99593;
  }
  html, body {
    margin: 0;
    width: 1200px;
    height: 960px;
    overflow: hidden;
    background: var(--backdrop);
  }
  .book-cover {
    position: absolute;
    left: 320px;
    top: 40px;
    width: 560px;
    height: 880px;
    background: radial-gradient(ellipse at 30% 40%, var(--cover-light) 0%, var(--cover) 50%, var(--cover-dark) 100%);
    color: var(--ink-light);
    box-shadow: 0 14px 40px rgba(0,0,0,0.12);
    overflow: hidden;
  }
  .author {
    position: absolute;
    top: 72px;
    left: 0;
    right: 0;
    text-align: center;
    font-family: "Josefin Sans", sans-serif;
    font-weight: 300;
    font-size: 24px;
    font-variant: small-caps;
    letter-spacing: 1.5px;
    margin: 0;
  }
  .title {
    position: absolute;
    top: 140px;
    left: 28px;
    width: 510px;
    height: 140px;
    margin: 0;
    font-weight: normal;
  }
  .title-line {
    position: absolute;
    font-family: "Josefin Sans", sans-serif;
    font-weight: 100;
    text-transform: uppercase;
    font-size: 58px;
    letter-spacing: 4px;
    line-height: 1;
  }
  .title-first { left: 0; top: 30px; }
  .title-script {
    position: absolute;
    left: 232px;
    top: -14px;
    font-family: "Dancing Script", cursive;
    font-size: 96px;
    color: var(--rose);
    line-height: 1;
  }
  .title-last { right: 0; top: 78px; }
  .subtitle {
    position: absolute;
    top: 300px;
    left: 40px;
    right: 40px;
    text-align: center;
    font-family: "Josefin Sans", sans-serif;
    font-weight: 300;
    font-size: 19px;
    font-variant: small-caps;
    letter-spacing: 1.2px;
    line-height: 1.3;
    margin: 0;
  }
  .cover-illustration {
    position: absolute;
    left: 130px;
    top: 360px;
    width: 300px;
    height: 500px;
    border-radius: 50% 50% 40% 40%;
    background: radial-gradient(ellipse at 55% 30%, var(--rose) 0%, rgba(185,149,147,0.55) 40%, rgba(95,117,115,0) 75%);
  }
</style>
</head>
<body>
  <main class="book-cover">
    <p class="author">Jana Roth</p>
    <h1 class="title">
      <span class="title-line title-first">Innere</span>
      <span class="title-script">Ruhe</span>
      <span class="title-line title-last">finden</span>
    </h1>
    <p class="subtitle">Wie aus kleinen Gewohnheiten jeden Tag neue<br>Gelassenheit im Alltag wächst</p>
    <div class="cover-illustration" role="img" aria-label="Linienzeichnung einer jungen Frau von hinten, die mit erhobenen Armen ein großes rosa Herz hält, ein zweites Herz schwebt neben ihr"></div>
  </main>
</body>
</html>
```